Web site design for Brivolt Software (www.brivoltsoftware-example.com)

Need the design as well as the html for the website. The brief is given in the attached file.
If possible, would like to use pencil sketches instead of images to give a unique look to the site.
Target Market(s)
small Software product companies
Industry/Entity Type
Software
Coding
Coded - Design and coding required
Number of Pages Required
5+ page

```html
<!DOCTYPE html>
<html lang="en">
<head>
<meta charset="utf-8">
<title>Brivolt Software — Driven by architecture</title>
<link rel="stylesheet" href="https://fonts.googleapis.com/css2?family=Special+Elite&family=Courier+Prime:wght@400;700&display=swap">
<style>
:root{
  --ink:#0c0c0d;
  --paper:#f2f0ea;
  --text:#e6e4de;
  --muted:#b9b6ae;
  --red:#b8322a;
  --red-soft:#d0453a;
  --band:rgba(20,20,22,.85);
  --line:rgba(255,255,255,.18);
}
*{box-sizing:border-box;margin:0;padding:0}
html,body{width:1200px;height:3850px;overflow:hidden}
body{
  position:relative;
  background:
    radial-gradient(ellipse 60% 30% at 50% 32%,rgba(60,40,30,.35),transparent 70%),
    radial-gradient(ellipse 50% 20% at 30% 8%,rgba(50,50,55,.35),transparent 70%),
    linear-gradient(180deg,#141416 0%,#0c0c0d 40%,#101012 100%);
  color:var(--text);
  font-family:"Special Elite","Courier Prime",monospace;
}
.abs{position:absolute}
.sketch{position:absolute;pointer-events:none}
.sketch-tower{left:760px;top:80px;width:420px;height:900px;
  background:radial-gradient(ellipse at 50% 40%,rgba(200,200,200,.08),transparent 70%)}
.sketch-fire{left:300px;top:620px;width:600px;height:420px;
  background:radial-gradient(ellipse at 50% 60%,rgba(170,90,40,.22),transparent 70%)}
.sketch-city{left:0;top:3380px;width:1200px;height:470px;
  background:linear-gradient(180deg,transparent 0%,rgba(90,90,95,.18) 40%,rgba(60,60,64,.25) 100%)}

/* nav */
.nav{position:absolute;top:0;left:0;width:1200px;height:86px;background:rgba(0,0,0,.55)}
.nav-links{position:absolute;top:50px;display:flex;gap:22px;font-family:"Courier Prime",monospace;font-size:15px;color:var(--text)}
.nav-left{left:16px}
.nav-right{right:16px}
.brand{position:absolute;left:0;width:1200px;top:12px;text-align:center}
.brand-name{font-family:"Special Elite",monospace;font-size:40px;line-height:1;letter-spacing:4px;color:var(--paper)}
.brand-tag{font-family:"Courier Prime",monospace;font-size:14px;letter-spacing:2px;color:var(--muted);margin-top:6px}

/* shared */
.quote{position:absolute;left:0;width:1200px;text-align:center;font-family:"Courier Prime",monospace;font-weight:700;font-size:20px;color:var(--paper)}
.tag-red{position:absolute;transform:translateX(-50%);left:600px;background:var(--red);color:#fff;font-size:16px;padding:4px 16px;font-family:"Courier Prime",monospace;font-weight:700}
.label{position:absolute;left:600px;transform:translateX(-50%);background:var(--paper);color:var(--ink);
  font-family:"Courier Prime",monospace;font-weight:700;font-size:17px;letter-spacing:2px;text-transform:uppercase;white-space:nowrap;
  padding:6px 22px;border:2px solid #fff;box-shadow:3px 3px 0 rgba(0,0,0,.5)}
.label::before,.label::after{content:"";position:absolute;top:50%;width:34px;border-top:2px solid var(--paper)}
.label::before{right:100%}
.label::after{left:100%}
.copy{font-size:15px;line-height:1.6;color:var(--text)}
.center{text-align:center}
.btn{display:inline-block;background:var(--paper);color:var(--ink);font-family:"Courier Prime",monospace;font-weight:700;font-size:17px;padding:4px 16px;border:2px solid #fff}
.arrow{position:absolute;width:46px;height:24px}

/* services */
.service{position:absolute;top:664px;width:250px;text-align:center}
.service-icon{width:44px;height:44px;border-radius:50%;background:var(--red);margin:0 auto 12px;display:flex;align-items:center;justify-content:center}
.service-title{font-family:"Courier Prime",monospace;font-weight:700;font-size:18px;letter-spacing:1px;color:var(--paper);margin-bottom:10px}
.service .copy{font-size:13px;line-height:1.45;height:76px}
.service .btn{margin-top:14px}

/* expertise */
.bridge{left:716px;top:1105px;width:440px;height:200px;
  background:linear-gradient(160deg,rgba(220,220,220,.18),rgba(120,120,120,.08));border:1px solid var(--line)}

/* engagement */
.model{position:absolute;width:520px}
.model-title{font-family:"Courier Prime",monospace;font-size:27px;letter-spacing:1px;color:var(--paper);margin-bottom:10px}
.model .copy{font-size:14px;line-height:1.55}

/* work */
.wanted{left:128px;top:2020px;width:456px;height:196px;
  background:linear-gradient(135deg,#a88a5e,#7b6040 60%,#5c462e);box-shadow:0 6px 18px rgba(0,0,0,.6)}
.wanted-title{position:absolute;left:160px;top:2028px;font-family:"Special Elite",monospace;font-size:34px;color:#2a1d10}
.wanted-copy{position:absolute;left:160px;top:2075px;width:395px;font-size:15px;line-height:1.4;color:#2a1d10}

/* testimonial */
.person{position:absolute;top:2548px;width:108px;height:108px;background:linear-gradient(180deg,#9a9a9a,#4a4a4a)}

/* partners */
.partner-band{left:0;top:2808px;width:1200px;height:60px;background:rgba(0,0,0,.7)}
.badge{position:absolute;top:2820px;width:130px;height:36px;border-radius:4px}
.btn-red{background:var(--red);color:#fff;border:none;font-size:15px;letter-spacing:1px;padding:6px 18px}

/* blog */
.card{position:absolute;top:3098px;width:266px;height:392px;background:var(--paper);color:var(--ink)}
.card-title{font-family:"Courier Prime",monospace;font-weight:700;font-size:16px;text-transform:uppercase;padding:14px 12px 6px;line-height:1.2}
.card-text{font-family:"Courier Prime",monospace;font-size:11px;line-height:1.35;padding:0 12px;color:#444}
.card-photo{position:absolute;left:0;top:100px;width:266px;height:256px;background:linear-gradient(180deg,#7d97b4,#3c5270 70%,#2a3548)}
.card-meta{position:absolute;left:0;bottom:0;width:266px;height:36px;display:flex;gap:14px;align-items:center;padding:0 12px;font-family:"Courier Prime",monospace;font-size:11px;color:#333}
.card-meta i{display:inline-block;width:8px;height:8px;background:var(--red);margin-right:4px}
.dots{position:absolute;top:3560px;left:550px;display:flex;gap:8px}
.dots span{width:26px;height:6px;background:var(--muted)}
.dots span.on{background:var(--red-soft)}

/* footer */
.footer-band{left:0;top:3590px;width:1200px;height:170px;background:var(--band)}
.contact{position:absolute;top:3612px;display:flex;gap:18px}
.contact-icon{flex:0 0 46px;height:46px;border-radius:50%;background:var(--paper);display:flex;align-items:center;justify-content:center}
.contact-title{font-family:"Courier Prime",monospace;font-size:19px;color:var(--paper);margin-bottom:6px}
.contact .copy{font-size:12px;line-height:1.45;color:var(--muted)}
.copyright{position:absolute;top:3785px;left:0;width:1200px;text-align:center;font-family:"Courier Prime",monospace;font-size:11px;color:var(--muted)}
</style>
</head>
<body>

<div class="sketch sketch-tower" role="img" aria-label="Pencil sketch of a gothic clock tower"></div>
<div class="sketch sketch-fire" role="img" aria-label="Pencil sketch of a glowing industrial scene"></div>
<div class="sketch sketch-city" role="img" aria-label="Pencil sketch of a cathedral skyline"></div>

<header class="nav">
  <nav class="nav-links nav-left"><span>Home</span><span>About Us</span><span>Services</span><span>Expertise</span><span>Stories</span></nav>
  <div class="brand">
    <div class="brand-name">BRIVOLT</div>
    <div class="brand-tag">Driven by architecture</div>
  </div>
  <nav class="nav-links nav-right"><span>Engagement Models</span><span>Agile</span><span>Case studies</span><span>Contact</span></nav>
</header>

<p class="quote" style="top:146px">'If I have seen further than others, it is by standing upon the shoulders of giants'</p>
<span class="tag-red" style="top:184px">Aristen</span>

<section>
  <h2 class="label" style="top:252px">About Us</h2>
  <p class="abs copy center" style="top:296px;left:0;width:1200px;font-family:'Courier Prime',monospace;font-weight:700;font-size:16px">We are passionate</p>
  <p class="abs copy center" style="top:356px;left:160px;width:880px">In our belief that a software product's architecture goes a long way in avoiding costly and complex upgrades. Our architecture driven approach makes sure that product upgrades are possible while maintaining productive and friendly user interfaces.</p>
  <p class="abs copy center" style="top:460px;left:160px;width:880px">Whether you are an established software product development company, a startup company or just a person with an idea, we would love to work with you. We work closely with clients to develop top level requirements, design the right team, and implement the software.</p>
</section>

<section>
  <h2 class="label" style="top:590px">Services</h2>
  <div class="service" style="left:38px">
    <div class="service-icon"><svg width="20" height="20" viewBox="0 0 20 20"><circle cx="10" cy="10" r="7" fill="none" stroke="#fff" stroke-width="2"/></svg></div>
    <h3 class="service-title">POC</h3>
    <p class="copy">Whether it is a mobile or web app prototype, or a more complex prototype, our engineers can understand the requirements...</p>
    <span class="btn">Read more</span>
  </div>
  <div class="service" style="left:322px">
    <div class="service-icon"><svg width="20" height="20" viewBox="0 0 20 20"><path d="M4 16 L10 4 L16 16 Z" fill="none" stroke="#fff" stroke-width="2"/></svg></div>
    <h3 class="service-title">BUILD PRODUCT</h3>
    <p class="copy">Our team of analysts, design thinkers and technologists work with client and end users to qualify and carve out a product...</p>
    <span class="btn">Read more</span>
  </div>
  <div class="service" style="left:606px">
    <div class="service-icon"><svg width="20" height="20" viewBox="0 0 20 20"><rect x="4" y="4" width="12" height="12" fill="none" stroke="#fff" stroke-width="2"/></svg></div>
    <h3 class="service-title">MAINTAIN PRODUCT</h3>
    <p class="copy">We have the ability to quickly understand large, legacy products, write scaffold test cases around them...</p>
    <span class="btn">Read more</span>
  </div>
  <div class="service" style="left:890px">
    <div class="service-icon"><svg width="20" height="20" viewBox="0 0 20 20"><circle cx="10" cy="10" r="3" fill="#fff"/><circle cx="10" cy="10" r="7" fill="none" stroke="#fff" stroke-width="2" stroke-dasharray="3 2"/></svg></div>
    <h3 class="service-title">ODC SETUP</h3>
    <p class="copy">We help in setting up Offshore Development Centers for small and medium software development companies...</p>
    <span class="btn">Read more</span>
  </div>
  <svg class="arrow" style="left:548px;top:940px" viewBox="0 0 46 24"><path d="M20 12 H2 M10 4 L2 12 L10 20" fill="none" stroke="#fff" stroke-width="2"/></svg>
  <svg class="arrow" style="left:606px;top:940px" viewBox="0 0 46 24"><path d="M26 12 H44 M36 4 L44 12 L36 20" fill="none" stroke="#fff" stroke-width="2"/></svg>
</section>

<section>
  <h2 class="label" style="top:1022px">Background and Expertise</h2>
  <p class="quote" style="top:1076px">'Look deep into nature, and you will understand everything better'</p>
  <span class="tag-red" style="top:1114px">Elstrand</span>
  <p class="abs copy" style="top:1202px;left:44px;width:640px">We are primarily server side programmers with expertise in large scale projects &amp; in IT Software development tools, Distributed software frameworks, Telecom and mediation software or Business intelligence. Over the years, we have been the trusted offshore product development partner for many startups and mid sized software product companies, and have built software products from scratch.[...]</p>
  <div class="abs bridge" role="img" aria-label="Pencil sketch of a steel truss bridge"></div>
</section>

<section>
  <h2 class="label" style="top:1466px">Engagement Models</h2>
  <div class="model" style="left:58px;top:1566px">
    <h3 class="model-title">ODC</h3>
    <p class="copy">We provide pure Outsourced product development for either new software development or product maintenance. Agile contracts and deliverable based compensation ensure value for customer and end user.</p>
  </div>
  <div class="model" style="left:632px;top:1566px">
    <h3 class="model-title">BOT</h3>
    <p class="copy">We help in setting up a team in India, gather expertise in your product and domain, grow the team and finally spin it off as your captive subsidiary.</p>
  </div>
  <div class="model" style="left:58px;top:1740px">
    <h3 class="model-title">EQUITY BASED</h3>
    <p class="copy">If you are a startup with very strong growth potential, we are interested. We can work out a equity-compensation mix that can help you get to market faster with a lower burn rate.</p>
  </div>
  <div class="model" style="left:632px;top:1740px;width:540px">
    <h3 class="model-title" style="font-size:25px;white-space:nowrap">ARCHITECTURAL &amp; PROCESS CONSULTANCY</h3>
    <p class="copy">ARCHITECTURAL AND PROCESS CONSULTANCY</p>
  </div>
</section>

<section>
  <h2 class="label" style="top:1934px">Work with us</h2>
  <div class="abs wanted" role="img" aria-label="Aged paper wanted poster"></div>
  <div class="wanted-title">WANTED</div>
  <p class="wanted-copy">Brivolt, is an employee driven company. Many of our policies are created and improved based on employees' requests. If you are interested in working with us, do write to hello@brivoltsoftware-example.com</p>
  <p class="abs copy" style="top:2026px;left:620px;width:540px">Brivolt works with startups and midsize product development companies. It uses design thinking and rigourous software development principles to build world class products.</p>
  <span class="abs btn" style="top:2142px;left:660px">Read More</span>
</section>

<section>
  <h2 class="label" style="top:2280px">Testimonial</h2>
  <p class="abs copy center" style="top:2372px;left:250px;width:700px;font-size:15px">Mara is officially the man! His level of professionalism and the understanding of the subject matter is the reason I will be looking forward</p>
  <p class="abs center" style="top:2450px;left:0;width:1200px;font-family:'Courier Prime',monospace;font-size:15px;letter-spacing:2px;color:var(--paper)">HALVERN GROUP</p>
  <p class="abs center" style="top:2474px;left:0;width:1200px;font-size:14px;color:var(--red-soft)">Mara Delvin</p>
  <p class="abs center" style="top:2498px;left:0;width:1200px;font-family:'Courier Prime',monospace;font-size:13px;letter-spacing:1px;color:var(--muted)">PRESIDENT DIRECTOR</p>
  <div class="person" style="left:416px" role="img" aria-label="Client portrait"></div>
  <div class="person" style="left:546px" role="img" aria-label="Client portrait"></div>
  <div class="person" style="left:676px" role="img" aria-label="Client portrait"></div>
  <svg class="arrow" style="left:168px;top:2592px" viewBox="0 0 46 24"><path d="M44 12 H2 M10 4 L2 12 L10 20" fill="none" stroke="#fff" stroke-width="2"/></svg>
  <svg class="arrow" style="left:986px;top:2592px" viewBox="0 0 46 24"><path d="M2 12 H44 M36 4 L44 12 L36 20" fill="none" stroke="#fff" stroke-width="2"/></svg>
</section>

<section>
  <h2 class="label" style="top:2732px">Partners</h2>
  <div class="abs partner-band"></div>
  <div class="badge" style="left:30px;background:#2aa3c8"></div>
  <div class="badge" style="left:245px;background:#2b5fa8"></div>
  <div class="badge" style="left:440px;background:#3b7bd6"></div>
  <div class="badge" style="left:612px;background:#4a6fb0"></div>
  <div class="badge" style="left:808px;background:#2f5e9e"></div>
  <div class="badge" style="left:1010px;background:#2b8fc2"></div>
  <span class="abs btn btn-red" style="top:2904px;left:512px">BE OUR PARTNERS</span>
</section>

<section>
  <h2 class="label" style="top:3040px">Latest Blogs</h2>
  <article class="card" style="left:176px">
    <h3 class="card-title">Consultancy Business</h3>
    <p class="card-text">Be consulting needs our in team that tends meet outstanding strategies for IT in various new year.</p>
    <div class="card-photo" role="img" aria-label="Business people in a meeting"></div>
    <div class="card-meta"><span><i></i>29-10-2017</span><span><i></i>Admin</span></div>
  </article>
  <article class="card" style="left:466px">
    <h3 class="card-title">News from Founder</h3>
    <p class="card-text">In 2018 we celebrate 10 years achievement of our company. Practices come from the founder to share now.</p>
    <div class="card-photo" role="img" aria-label="Founder speaking at an event"></div>
    <div class="card-meta"><span><i></i>25-09-2017</span><span><i></i>Admin</span></div>
  </article>
  <article class="card" style="left:756px">
    <h3 class="card-title">Ut wisi enim ad minim</h3>
    <p class="card-text">Lorem ipsum dolor sit amet, consectetuer adipiscing elit, sed diam nonummy nibh euismod tincidunt.</p>
    <div class="card-photo" role="img" aria-label="Colleagues shaking hands"></div>
    <div class="card-meta"><span><i></i>11-09-2017</span><span><i></i>Admin</span></div>
  </article>
  <div class="dots"><span class="on"></span><span class="on"></span><span></span></div>
</section>

<footer>
  <div class="abs footer-band"></div>
  <div class="contact" style="left:154px">
    <div class="contact-icon"><svg width="20" height="22" viewBox="0 0 20 22"><path d="M10 21 C4 13 3 11 3 8 a7 7 0 0 1 14 0 c0 3-1 5-7 13z" fill="var(--ink)"/><circle cx="10" cy="8" r="2.5" fill="var(--paper)"/></svg></div>
    <div>
      <h4 class="contact-title">Address</h4>
      <p class="copy">Brivolt Software (I)<br>Pvt Ltd, Harbour Point,<br>Office 4B, Lantern Road,<br>Northgate Park,<br>Riverton 400123, India</p>
    </div>
  </div>
  <div class="contact" style="left:448px">
    <div class="contact-icon"><svg width="20" height="20" viewBox="0 0 20 20"><path d="M4 2 L8 2 L9 6 L7 8 C8 11 9 12 12 13 L14 11 L18 12 L18 16 C18 17 17 18 16 18 C8 18 2 12 2 4 C2 3 3 2 4 2z" fill="var(--ink)"/></svg></div>
    <div>
      <h4 class="contact-title">Phone</h4>
      <p class="copy">+00-0 000 0000 00<br>Mon-Fri 9:00am - 6:00pm</p>
    </div>
  </div>
  <div class="contact" style="left:746px">
    <div class="contact-icon"><svg width="22" height="16" viewBox="0 0 22 16"><rect x="1" y="1" width="20" height="14" fill="var(--ink)"/><path d="M1 1 L11 9 L21 1" fill="none" stroke="var(--paper)" stroke-width="1.5"/></svg></div>
    <div>
      <h4 class="contact-title">Mail</h4>
      <p class="copy">support@brivoltsoftware-example.com</p>
    </div>
  </div>
  <p class="copyright">© 2005-2018 brivoltsoftware-example.com. All rights reserved.</p>
</footer>

</body>
</html>
```